依頼詳細
販売する水産物ですが、安売りではなく単価の高い水産物なので美味しさだけでなく高級感も感じさせるデザインで白を基調としたイメージでお願いします。
記載項目
浜栄水産/0983-47-1852/http://www.kaisuzuka.co.jp//潮風の便り/ロゴ(webサイトのロゴを使ってください。)
サイズ
基本はB2ですがお任せします。
ページ数
片面
希望イメージ
シンプル 複雑
単色 カラフル
暗い 明るい
日常 高級
遊び心 厳粛
未来的 伝統的
女性的 男性的
希望する色
白を基調とした高級感が伝わるような感じでお願いします。
納品ファイル
• 高解像度JPG (.jpg)
• イラストレーター形式 (.ai)
補足説明
参考URL/http://www.kaisuzuka.co.jp/
当社の水産物は大都市圏で高い評価をいただいている水産物です。
その理由として他社に負けない取扱いで出荷しています。
その思いをポスターに伝える表現でお願いします。

ポスターで使う水産物の写真は
http://www.kaisuzuka.co.jp/blog/
から利用してください。

天然の真鯛の写真はは当社の看板商品なので必ず使用してください。
・真鯛の写真が少なかったのでブログに追加しました。

・ロゴですが綺麗に収まるのであれば利用しなくても大丈夫です。
高級感が伝わり産地がわかるポスターであればお任せします。
■ 選んだ理由

今回、どの案も素晴らしく決定にかなり悩みました。
その中でシンプルで伝えたいことが分かりやすく、ブランド名がはっきり分かりやすい案を、数種類選びだし関係する方からの意見も聞き総合評価で決定しました。

■ 提案者全員のお礼・コメント

今回、提案していただい方々ありがとうございました。
どの案も素晴らしく予算があればもっとと思うことが多々あり大変でした。

今回、審査途中でコメントを入れようか悩みましたが提案の意味や提案者の素の能力をできるだけ見極めたいのでしませんでした。

このような時間をかけた提案をした方々に、何も返答しない非礼をここでお詫びさせてください。

また、他の案件も考えているので、出来ればまたよろしくお願い致します。
ありがとうございました。

```html
<!DOCTYPE html>
<html lang="ja">
<head>
<meta charset="utf-8">
<title>潮風の便り ポスター</title>
<link rel="stylesheet" href="https://fonts.googleapis.com/css2?family=Shippori+Mincho:wght@400;600;800&family=Cormorant+Garamond:wght@500;600&display=swap">
<style>
:root{
  --paper:#ffffff;
  --ink:#1d1d1d;
  --ink-soft:#444444;
  --map-red:#b3261e;
  --map-red-deep:#8c1a14;
  --tai:#d9816f;
  --tai-deep:#b85a48;
  --hiramasa:#a7b296;
  --hiramasa-deep:#76845f;
  --mejina:#6a7370;
  --mejina-deep:#3a413f;
  --crab:#c0603a;
  --crab-deep:#7e3318;
}
*{margin:0;padding:0;box-sizing:border-box}
html,body{width:849px;height:1200px;overflow:hidden;background:var(--paper)}
.poster{position:relative;width:849px;height:1200px;background:var(--paper);color:var(--ink);font-family:"Shippori Mincho",serif}
.abs{position:absolute}

.map{left:0;top:0;width:300px;height:265px;background:linear-gradient(160deg,var(--map-red) 0%,var(--map-red-deep) 70%,#c9706a 100%);border-bottom-right-radius:60% 45%}

.title{right:95px;top:30px;writing-mode:vertical-rl;font-size:104px;font-weight:600;line-height:1;letter-spacing:0}
.ruby{font-size:18px;writing-mode:vertical-rl;font-weight:400;color:var(--ink-soft);letter-spacing:4px}
.ruby-a{right:62px;top:60px}
.ruby-b{right:62px;top:345px}

.place{left:355px;top:182px;font-size:24px;font-weight:800;letter-spacing:2px}
.place-en{left:330px;top:222px;font-family:"Cormorant Garamond",serif;font-size:28px;font-weight:600}
.lead{left:212px;top:283px;width:385px;font-size:10.5px;line-height:1.75;color:var(--ink-soft)}
.lead p{margin-bottom:7px}

.photo{border-radius:50%}
.photo-tai{left:42px;top:415px;width:445px;height:200px;background:radial-gradient(ellipse at 40% 45%,var(--tai) 0%,var(--tai-deep) 100%)}
.photo-hiramasa{left:430px;top:560px;width:390px;height:105px;background:radial-gradient(ellipse at 45% 50%,var(--hiramasa) 0%,var(--hiramasa-deep) 100%)}
.photo-mejina{left:42px;top:760px;width:230px;height:140px;background:radial-gradient(ellipse at 45% 50%,var(--mejina) 0%,var(--mejina-deep) 100%)}
.photo-crab{left:360px;top:855px;width:140px;height:120px;background:radial-gradient(ellipse at 50% 50%,var(--crab) 0%,var(--crab-deep) 100%)}

.label{display:flex;align-items:baseline;gap:10px;white-space:nowrap}
.label .en{font-family:"Cormorant Garamond",serif;font-size:19px;font-weight:600}
.label .jp{font-size:34px;font-weight:800;letter-spacing:2px}
.label-tai{left:170px;top:622px}
.label-hiramasa{right:45px;top:676px}
.label-mejina{left:42px;top:902px}
.label-crab{left:515px;top:892px}

.note{font-size:9px;line-height:1.65;color:var(--ink-soft)}
.note-tai{left:42px;top:672px;width:380px}
.note-hiramasa{left:450px;top:730px;width:370px}
.note-mejina{left:42px;top:950px;width:280px}
.note-crab{left:520px;top:945px;width:300px}
.note-extra{left:345px;top:990px;width:160px}

.footer{left:305px;top:1110px;font-size:19px;font-weight:600;letter-spacing:3px;white-space:nowrap}
</style>
</head>
<body>
<main class="poster">
  <div class="abs map" role="img" aria-label="九州を中心とした日本地図、佐伯市の位置を示す赤い地図"></div>

  <h1 class="abs title">潮風の便り</h1>
  <span class="abs ruby ruby-a">しおかぜ</span>
  <span class="abs ruby ruby-b">たよ</span>

  <div class="abs place">大分県佐伯市</div>
  <div class="abs place-en">from Saiki,Oita</div>

  <div class="abs lead">
    <p>「潮風の便り」とは、浜栄水産が独自の目利きで選び抜いた、豊後水道で水揚げされた最高品質の水産物のことです。</p>
    <p>黒潮と瀬戸内の潮がぶつかる豊後水道で育った魚介を、早朝の水揚げから出荷まで一尾ずつ丁寧に扱い、鮮度と身の締まりを守って大都市圏へお届けしています。</p>
    <p>「潮風の便り」は確かな品質の証です。</p>
  </div>

  <div class="abs photo photo-tai" role="img" aria-label="天然真鯛の写真"></div>
  <div class="abs photo photo-hiramasa" role="img" aria-label="平政の写真"></div>
  <div class="abs photo photo-mejina" role="img" aria-label="黒目品の写真"></div>
  <div class="abs photo photo-crab" role="img" aria-label="朝日蟹の写真"></div>

  <div class="abs label label-tai"><span class="en">Madai</span><span class="jp">真鯛</span></div>
  <div class="abs label label-hiramasa"><span class="en">Hiramasa</span><span class="jp">平政</span></div>
  <div class="abs label label-mejina"><span class="en">Kuromejina</span><span class="jp">黒目品</span></div>
  <div class="abs label label-crab"><span class="en">Kuromejina</span><span class="jp">朝日蟹</span></div>

  <p class="abs note note-tai">豊後水道の速い潮に揉まれて育った天然真鯛。身は締まり、上品な甘みと香りが特長です。活け締めで鮮度を保ち出荷します。</p>
  <p class="abs note note-hiramasa">回遊する天然の平政は、脂のりと歯ごたえの良さが魅力。刺身や寿司種として料理人から高い評価をいただいています。</p>
  <p class="abs note note-mejina">磯の香りをまとう黒目品。冬場は脂がのり、刺身や煮付けで深い旨みを味わえます。</p>
  <p class="abs note note-crab">鮮やかな朱色の朝日蟹。濃厚な味噌と甘い身が楽しめる希少な蟹です。</p>
  <p class="abs note note-extra">水揚げから出荷まで一貫した管理で産地の味をお届けします。</p>

  <div class="abs footer">豊後水道　浜栄水産</div>
</main>
</body>
</html>
```